Design professional label for greener chemicals (cleaning and lubrication) brand

Design a b2b professional label that is based on the examples given.
Size: 135 x 200 mm, please use text of the label description doc (only the kaltro stainless steel polish example design document has the right text and size)
It should include:
1. Logo, can be fully changed except the shape of "KALTRO", colors and fonts of the rest can be customized
2. Focus should be on professional market, we would like to express the professionalism and high quality of the product
3. Focus should be on our brand name "KALTRO BRIGHTER COMPOUNDS"
4. Should include product name, product description, danger sentences, danger symbol, user instructions, image
5. Should include numbers that explain what the product does: 1. Prewash 2. Clean 3. Protect 4. Preserve and highlight number 2.

Target Market(s)

Professional cleaning companies, steel industry, food industry, pharmacy industry

Industry/Entity Type

Cleaning industry, steel industry, food industry, boat cleaning, car cleaning, professional lubrication

Font styles to use
Sans Serif

Requirements
Must have
• Professional look, clean look, image, focus on our brand name
Nice to have
• Numbers (see explanation), label divided in three parts (logo and product name and image in the middle as the highlight)

```html
<!DOCTYPE html>
<html lang="en">
<head>
<meta charset="utf-8">
<title>Kaltro Stainless Steel Polish – Label</title>
<link rel="stylesheet" href="https://fonts.googleapis.com/css2?family=Fira+Sans:wght@400;600;700;800&family=Fira+Sans+Condensed:wght@400;700&display=swap">
<style>
  :root{
    --blue:#1f74b8;
    --blue-deep:#1766a6;
    --blue-light:#2f8fd3;
    --green:#8cc04b;
    --white:#ffffff;
    --ink:#1d1d1f;
    --grey:#a9a9ad;
    --red:#e3001b;
  }
  *{margin:0;padding:0;box-sizing:border-box}
  html,body{width:839px;height:1200px;overflow:hidden;background:var(--white)}
  body{font-family:"Fira Sans",sans-serif;color:var(--white);position:relative}
  .label{position:absolute;left:30px;top:336px;width:780px;height:527px;overflow:hidden}
  .label-bg{position:absolute;inset:0}
  .abs{position:absolute}

  .brand-name{left:282px;top:30px;width:220px;text-align:center;font-weight:800;font-size:66px;line-height:1;color:var(--blue);letter-spacing:-1px}
  .brand-tagline{left:282px;top:108px;width:220px;text-align:center;font-size:13px;letter-spacing:2.6px;color:var(--green);font-weight:400}

  .product-title{left:264px;top:160px;font-weight:800;font-size:41px;line-height:36px;letter-spacing:.3px}
  .product-title .green{color:var(--green);display:block}
  .product-title .blue{color:var(--blue);display:block}
  .product-claims{left:266px;top:275px;font-size:13px;line-height:17.6px;color:var(--ink);text-transform:uppercase}

  .use-title{left:293px;top:411px;font-weight:700;font-size:12px}
  .use-item{top:437px;width:80px;text-align:center;font-size:10px;line-height:13px}
  .use-item svg{display:block;margin:0 auto 10px}

  .company{left:30px;top:345px;font-size:9.6px;line-height:13px;width:200px}
  .company b{font-weight:700;display:block}
  .company .line{display:flex;align-items:flex-start;gap:4px;margin-left:-16px}
  .company .line svg{flex:none;width:12px;height:12px;margin-top:0.5px}
  .company .indent{padding-left:0}
  .company .gap{height:6px}

  .info-title{left:542px;top:28px;width:222px;font-weight:700;font-size:11.8px;line-height:15px}
  .info-text{left:542px;top:60px;width:220px;font-size:11.6px;line-height:15.6px;text-align:justify}

  .steps-head{left:536px;top:180px;width:229px;height:23px;background:var(--green);font-size:11px;font-weight:600;padding:5px 0 0 7px;letter-spacing:.2px}
  .steps{left:536px;top:203px;width:229px;height:112px;background:var(--white);color:var(--ink);list-style:none;padding:8px 6px 0 7px;font-size:9.4px;line-height:12.3px}
  .steps li{display:flex;gap:6px;margin-bottom:2.6px}
  .steps .num{flex:none;width:11px;height:11px;border-radius:50%;background:var(--green);color:var(--white);font-size:7.5px;font-weight:700;text-align:center;line-height:11px}

  .danger{left:536px;top:323px;width:229px;height:90px;background:var(--white);border:1.2px solid var(--ink);display:flex;gap:6px;padding:4px 6px 0 6px}
  .danger svg{flex:none;margin-top:14px}
  .danger p{font-family:"Fira Sans Condensed",sans-serif;font-size:7.6px;line-height:10.6px;color:var(--ink);text-align:justify}
  .danger strong{color:var(--red);font-weight:700}

  .meta{left:542px;top:433px;font-size:10px;line-height:13px}
  .meta .gap{height:13px}
</style>
</head>
<body>
<div class="label">
  <svg class="label-bg" width="780" height="527" viewBox="0 0 780 527">
    <defs>
      <linearGradient id="bg-blue" x1="0" y1="0" x2="1" y2="1">
        <stop offset="0" stop-color="#1766a6"/>
        <stop offset=".55" stop-color="#2a86cc"/>
        <stop offset="1" stop-color="#1b6eb0"/>
      </linearGradient>
      <linearGradient id="ring-grey" x1="0" y1="0" x2="1" y2="0">
        <stop offset="0" stop-color="#8f8f94"/>
        <stop offset=".5" stop-color="#d9d9dc"/>
        <stop offset="1" stop-color="#9c9ca1"/>
      </linearGradient>
      <linearGradient id="photo-tone" x1="0" y1="0" x2="0" y2="1">
        <stop offset="0" stop-color="#eef0f1"/>
        <stop offset=".55" stop-color="#d6dadd"/>
        <stop offset="1" stop-color="#c2c7cb"/>
      </linearGradient>
    </defs>
    <rect width="780" height="527" fill="url(#bg-blue)"/>
    <ellipse cx="345" cy="118" rx="203" ry="278" fill="url(#ring-grey)"/>
    <ellipse cx="356" cy="124" rx="184" ry="265" fill="#ffffff"/>
    <circle cx="115" cy="232" r="91" fill="#9a9a9f"/>
    <circle cx="115" cy="232" r="86" fill="url(#photo-tone)" role="img" aria-label="Photo: gloved hand polishing a stainless steel surface with a green cloth"/>
    <circle cx="398" cy="351" r="70" fill="#1d6db0"/>
    <circle cx="398" cy="351" r="66" fill="url(#photo-tone)" role="img" aria-label="Photo: gloved hand polishing stainless steel with a green cloth"/>
    <circle cx="486" cy="297" r="30" fill="var(--green)"/>
    <circle cx="486" cy="297" r="22" fill="none" stroke="#ffffff" stroke-width="2"/>
  </svg>

  <div class="abs brand-name">KALTRO</div>
  <div class="abs brand-tagline">BRIGHTER COMPOUNDS</div>

  <h1 class="abs product-title"><span class="green">STAINLESS</span><span class="green">STEEL</span><span class="blue">POLISH</span></h1>
  <p class="abs product-claims">Restore steel<br>surfaces<br>hologram<br>free</p>

  <div class="abs use-title">USE ON/FOR</div>
  <div class="abs use-item" style="left:267px">
    <svg width="32" height="34" viewBox="0 0 32 34" fill="none" stroke="#fff" stroke-width="1.6" stroke-linejoin="round">
      <rect x="11" y="3" width="10" height="6"/><rect x="7" y="9" width="18" height="7"/>
      <path d="M2 16h28l-5 14H7z"/><path d="M16 18v9"/>
    </svg>
    <div style="padding-top:10px">Boats</div>
  </div>
  <div class="abs use-item" style="left:344px;top:425px">
    <svg width="34" height="46" viewBox="0 0 34 46" fill="none" stroke="#fff" stroke-width="1.6">
      <rect x="21" y="2" width="7" height="22"/><path d="M3 45V24l9-6v6l9-6v6h10v21z"/>
      <rect x="8" y="30" width="5" height="4"/><rect x="16" y="30" width="5" height="4"/>
      <rect x="8" y="37" width="5" height="4"/><rect x="16" y="37" width="5" height="4"/>
    </svg>
    <div>Industrial steel<br>surfaces</div>
  </div>
  <div class="abs use-item" style="left:428px">
    <svg width="42" height="36" viewBox="0 0 42 36" fill="none" stroke="#fff" stroke-width="1.8">
      <rect x="1" y="1" width="40" height="34"/><rect x="5" y="5" width="32" height="26"/>
      <path d="M21 5v26"/><path d="M10 12v8M32 12v8"/>
    </svg>
    <div style="padding-top:2px">Stainless steel<br>kitchens</div>
  </div>

  <div class="abs company">
    <b>KALTRO LABORATORIES INT. B.V.</b>
    <b>NETHERLAND</b>
    <div class="line"><svg viewBox="0 0 12 12" fill="none" stroke="#fff" stroke-width="1.1"><circle cx="6" cy="6" r="5.3"/><path d="M6 9.5 3.8 6.3a2.6 2.6 0 1 1 4.4 0z"/></svg><span>Postbus 48120</span></div>
    <div class="line"><span style="width:12px"></span><span>5100 AB Dalmere (NL)</span></div>
    <div class="line"><svg viewBox="0 0 12 12" fill="#fff"><circle cx="6" cy="6" r="6"/><path d="M3.6 3.2l1.4-.4.8 1.7-.9.7c.4.9 1 1.6 1.9 2l.7-.9 1.7.8-.4 1.4C6.2 8.6 3.4 5.8 3.6 3.2z" fill="#1f74b8"/></svg><span>Phone NL +31 400 12 34 56</span></div>
    <div class="gap"></div>
    <b>BELGIUM</b>
    <div class="line"><svg viewBox="0 0 12 12" fill="none" stroke="#fff" stroke-width="1.1"><circle cx="6" cy="6" r="5.3"/><path d="M6 9.5 3.8 6.3a2.6 2.6 0 1 1 4.4 0z"/></svg><span>Lindenlaan 24 bus 3</span></div>
    <div class="line"><span style="width:12px"></span><span>3600 Verhout (B)</span></div>
    <div class="line"><svg viewBox="0 0 12 12" fill="#fff"><circle cx="6" cy="6" r="6"/><path d="M3.6 3.2l1.4-.4.8 1.7-.9.7c.4.9 1 1.6 1.9 2l.7-.9 1.7.8-.4 1.4C6.2 8.6 3.4 5.8 3.6 3.2z" fill="#1f74b8"/></svg><span>Phone B: +32 10 00 45 67</span></div>
    <div class="gap"></div>
    <div class="line"><svg viewBox="0 0 12 12" fill="none" stroke="#fff" stroke-width="1"><circle cx="6" cy="6" r="5.2"/><ellipse cx="6" cy="6" rx="2.3" ry="5.2"/><path d="M1 6h10"/></svg><span style="font-weight:700">www.kaltrocompounds.com</span></div>
    <div class="line"><span style="width:12px"></span><span>hello@kaltrocompounds.com</span></div>
  </div>

  <h2 class="abs info-title">PROFESSIONAL STAINLESS STEEL POLISH</h2>
  <p class="abs info-text">Brilvex is a mildly abrasive cleansing cream with preservative properties. For removing stubborn dirt, water stains and deposits on stainless steel with a hologram free finish. Brilvex is non-tox and safe to use.</p>

  <div class="abs steps-head">USER INSTRUCTIONS</div>
  <ol class="abs steps">
    <li><span class="num">1</span><span>Shake before use.</span></li>
    <li><span class="num">2</span><span>Apply with a damp brush, sponge or pad.</span></li>
    <li><span class="num">3</span><span>Adjust rubbing pressure and duration to the persistence of the soiling.</span></li>
    <li><span class="num">4</span><span>Add water as needed while rubbing, rub in the direction of the structure.</span></li>
    <li><span class="num">5</span><span>Rinse with clean water.</span></li>
  </ol>

  <div class="abs danger">
    <svg width="50" height="50" viewBox="0 0 50 50" fill="#fff" stroke="var(--red)" stroke-width="1.8">
      <path d="M25 2l11 11-11 11-11-11z"/><path d="M13 14l11 11-11 11L2 25z"/>
      <path d="M37 14l11 11-11 11-11-11z"/><path d="M25 26l11 11-11 11-11-11z"/>
      <g stroke="#111" stroke-width="1.6" fill="none">
        <path d="M25 8v7M22 17h6"/><circle cx="13" cy="24" r="2.5"/><path d="M9 28l8-1M9 27l8 1"/>
        <path d="M37 20v6"/><path d="M21 40h8M25 32v6"/>
      </g>
      <circle cx="37" cy="29" r="1" fill="#111" stroke="none"/>
    </svg>
    <p><strong>DANGER:</strong> Causes severe skin burns and eye damage. Wear protective gloves, protective clothing, eye protection, face protection. IF SWALLOWED: rinse mouth – DO NOT induce vomiting. Immediately call a POISON CENTER, a physician. IF ON SKIN (or hair): Take off immediately all contaminated clothing.</p>
  </div>

  <div class="abs meta">
    <div>Expiring dates:</div>
    <div class="gap"></div>
    <div>Batch number: see packaging.</div>
    <div>Net volume: see packaging.</div>
    <div>Label number: 23092021</div>
  </div>
</div>
</body>
</html>
```